Flyer for annual KESTREL GATHERING 2020

I would like a church event flyer designed. The event is called "KESTREL GATHERING 2020". I am looking for a professional, yet catchy design that uses our brand colors and logo creatively while communicating key information of the event effectively.

1. The logo is attached in two color formats. The designer has the choice to use them as he/she want.

2. The location of the event is: Lindow Community Center, 482 Tamsey Street, Portland, ME 04117

3. Time and date of event. The designer can organize and format the date and time as he/she pleases.
Thursday December 31st @ 6:30PM
Friday January 1st @ 6:30PM
Saturday 2nd @ 6:30PM
Sunday 3rd @ 4:30PM

4. The topic of the event is "In Fire and On Fire". The designer is free to use this phrase as he/she pleases to create a good composition.

5. Speaker: Prophet Marcus Obele (2 pictures of the speaker to choose from are attached)

6. Contact information: contact@harvestmill.org - Telephone number: 207 555 0142

7. I would also like the following three words on the flyer. These words describe the focus of the event: FIRE, REVIVAL, PROPHETIC

Target Market(s)

Young adults

Font styles to use
Sans Serif

Requirements
Must have
• Logo, speaker's picture
Should not have
• cross image, church image

```html
<!DOCTYPE html>
<html lang="en">
<head>
<meta charset="utf-8">
<title>Kestrel Gathering 2020 – Flyer</title>
<link rel="stylesheet" href="https://fonts.googleapis.com/css2?family=Montserrat:ital,wght@0,400;0,600;0,700;1,700&family=Oswald:wght@500;600&family=Poppins:wght@400;500&display=swap">
<style>
:root{
  --navy:#0f2a4a;
  --orange:#f7941d;
  --white:#ffffff;
  --stage:#8a8a8a;
  --red:#d9262a;
}
*{box-sizing:border-box;margin:0;padding:0}
html,body{width:1200px;height:1200px;overflow:hidden;background:var(--stage)}
.flyer{
  position:absolute;left:204px;top:87px;width:990px;height:1282px;
  transform:scale(.8);transform-origin:0 0;
  background:var(--white);overflow:hidden;
  font-family:"Montserrat",sans-serif;color:var(--navy);
}
.backdrop{position:absolute;inset:0}
.abs{position:absolute}
.contact{left:58px;top:98px}
.contact-label{color:var(--orange);font-size:24px;font-weight:600;letter-spacing:.5px}
.contact-line{font-size:25px;margin-top:8px;font-weight:400}
.contact-line b{font-weight:700}
.brand{right:56px;top:150px;display:flex;align-items:center;gap:12px}
.brand-dot{width:26px;height:26px;border-radius:50%;background:var(--orange)}
.brand-name{font-size:42px;font-weight:700;color:var(--navy);letter-spacing:1px}
.title{left:56px;top:345px;font-family:"Poppins",sans-serif;font-weight:400;line-height:90px;letter-spacing:-5px}
.title span{display:block;font-size:92px}
.title .accent{color:var(--orange)}
.title .light{color:var(--white)}
.focus{left:60px;top:626px;color:var(--white);font-size:30px;font-weight:700;font-style:italic;word-spacing:8px}
.note{left:580px;top:330px;width:300px;height:270px;background:var(--white);transform:rotate(-8deg);
  box-shadow:4px 8px 14px rgba(0,0,0,.35);display:flex;flex-direction:column;align-items:center;justify-content:center;
  font-family:"Oswald",sans-serif;color:var(--navy)}
.note-big{font-size:84px;font-weight:600;line-height:1;letter-spacing:-1px;transform:scaleX(.85)}
.note-band{background:var(--orange);color:var(--white);font-family:"Montserrat",sans-serif;font-size:44px;letter-spacing:12px;
  padding:2px 16px 2px 28px;margin:6px 0;font-weight:400}
.pin{left:700px;top:295px;width:34px;height:34px;border-radius:50%;background:var(--red);box-shadow:2px 4px 6px rgba(0,0,0,.3)}
.dates{left:58px;top:768px;display:grid;grid-template-columns:310px 300px;row-gap:28px}
.date{display:flex;align-items:center;gap:12px}
.cal{width:92px;height:95px;background:var(--white);border-radius:6px;position:relative;overflow:hidden;box-shadow:0 1px 3px rgba(0,0,0,.08)}
.cal-top{height:34px;background:var(--orange);color:var(--white);font-size:14px;font-weight:700;display:flex;align-items:flex-end;justify-content:center;padding-bottom:3px;gap:6px}
.cal-top i{font-style:normal;font-weight:400}
.cal-day{color:var(--orange);font-size:52px;font-weight:700;text-align:center;line-height:58px}
.cal-ring{position:absolute;top:-4px;width:7px;height:18px;border-radius:4px;background:var(--navy)}
.date-text{font-size:27px;font-weight:700;line-height:1.22}
.date-text em{font-style:normal;color:var(--orange)}
.venue{left:58px;top:1012px}
.venue-name{font-size:34px;font-weight:600}
.venue-addr{font-size:22px;margin-top:6px}
.venue-room{font-size:15px;margin-top:6px}
.speaker-tag{left:58px;top:1125px;width:225px;height:62px;background:var(--orange);color:var(--white);font-size:32px;font-weight:700;display:flex;align-items:center;justify-content:center}
.speaker-name{left:60px;top:1195px;font-size:35px;font-weight:700}
</style>
</head>
<body>
<div class="flyer">
  <svg class="backdrop" width="990" height="1282" viewBox="0 0 990 1282">
    <defs>
      <linearGradient id="creamFade" x1="0" y1="0" x2="0" y2="1">
        <stop offset="0" stop-color="#fdf3ea"/><stop offset="1" stop-color="#fde6cc"/>
      </linearGradient>
      <linearGradient id="bandTone" x1="0" y1="0" x2="1" y2="0">
        <stop offset="0" stop-color="#0f2a4a"/><stop offset=".55" stop-color="#14506a"/><stop offset="1" stop-color="#0f2a4a"/>
      </linearGradient>
      <linearGradient id="photoTone" x1="0" y1="0" x2="0" y2="1">
        <stop offset="0" stop-color="#3a2a24"/><stop offset=".35" stop-color="#d4532a"/><stop offset="1" stop-color="#1d2d55"/>
      </linearGradient>
    </defs>
    <path d="M0 680 C250 760 450 720 620 660 L990 640 L990 1282 L0 1282 Z" fill="url(#creamFade)"/>
    <path d="M0 1130 C200 1090 450 1110 620 1150 L620 1282 L0 1282 Z" fill="var(--white)"/>
    <path d="M0 232 C250 205 520 212 760 285 C520 240 240 250 0 295 Z" fill="var(--orange)"/>
    <path d="M560 700 C700 610 850 585 990 598 L990 650 C860 628 720 650 560 720 Z" fill="var(--orange)"/>
    <path d="M0 290 C250 235 560 235 800 305 L990 410 L990 605 C820 580 680 620 560 670 C380 750 180 745 0 690 Z" fill="url(#bandTone)" role="img" aria-label="Blue-toned photo of a white dove in flight behind the title"/>
    <path d="M500 1282 L620 1180 L640 820 C680 690 760 640 850 640 C920 645 960 680 990 720 L990 1282 Z" fill="url(#photoTone)" role="img" aria-label="Photo of the speaker seated, wearing glasses and an orange-red blazer"/>
  </svg>

  <div class="abs contact">
    <div class="contact-label">CONTACT INFORMATION:</div>
    <div class="contact-line">contact@harvestmill.org</div>
    <div class="contact-line"><b>207 555 0142 |</b> www.<b>harvestmill</b>.org</div>
  </div>

  <div class="abs brand">
    <div class="brand-dot"></div>
    <div class="brand-name">HARVEST MILL</div>
  </div>

  <h1 class="abs title">
    <span class="accent">KESTREL</span>
    <span class="light">GATHERING</span>
    <span class="accent">2020</span>
  </h1>
  <div class="abs focus">Fire, Revival, Prophetic</div>

  <div class="abs note">
    <div class="note-big">IN FIRE</div>
    <div class="note-band">AND</div>
    <div class="note-big">ON FIRE</div>
  </div>
  <div class="abs pin"></div>

  <div class="abs dates">
    <div class="date">
      <div class="cal"><span class="cal-ring" style="left:20px"></span><span class="cal-ring" style="left:65px"></span><div class="cal-top">DEC.<i>2020</i></div><div class="cal-day">31</div></div>
      <div class="date-text">Thursday<br>at <em>6:30PM</em></div>
    </div>
    <div class="date">
      <div class="cal"><span class="cal-ring" style="left:20px"></span><span class="cal-ring" style="left:65px"></span><div class="cal-top">JAN.<i>2021</i></div><div class="cal-day">01</div></div>
      <div class="date-text">Friday<br>at <em>6:30PM</em></div>
    </div>
    <div class="date">
      <div class="cal"><span class="cal-ring" style="left:20px"></span><span class="cal-ring" style="left:65px"></span><div class="cal-top">JAN.<i>2021</i></div><div class="cal-day">02</div></div>
      <div class="date-text">Saturday<br>at <em>6:30PM</em></div>
    </div>
    <div class="date">
      <div class="cal"><span class="cal-ring" style="left:20px"></span><span class="cal-ring" style="left:65px"></span><div class="cal-top">JAN.<i>2021</i></div><div class="cal-day">03</div></div>
      <div class="date-text">Sunday<br>at <em>4:30PM</em></div>
    </div>
  </div>

  <div class="abs venue">
    <div class="venue-name">Lindow Community Center</div>
    <div class="venue-addr">482 Tamsey Street, Portland, ME 04117</div>
    <div class="venue-room">(Room: Renaissance)</div>
  </div>

  <div class="abs speaker-tag">SPEAKER:</div>
  <div class="abs speaker-name">Prophet Marcus Obele</div>
</div>
</body>
</html>
```